Letterhead needed using basic elements of our new logo!

We have just had a new logo and business card created on Pixel Harbor and now would like a new letterhead for our company re-branding. Our logo inspires trust, professionalism and confidence and we would like to mirror that in our letterhead. We would like to use elements in our logo (as well as the logo itself, obviously), but understand with only a header and the ability to print in black and white, we are somewhat limited. We have also won the Resident's Pick Medal for best Property Management Company in our city and would like to somehow include that small banner (see uploaded file) in the letterhead, without it clashing?

Text to include:
Stonebrook Property Management (and logo)
C-214 Marlowe Ave, Winnipeg, MB R2K 3P7
Ph: 204-738-2915
Fax: 1-888-276-9413
Email: customerservice@stonebrookpropertymanagement.example
Web: www.stonebrookpropertymanagement.example

Pasted below is our mission, vision and branding statements to help with the project:

Mission Statement

Provide the highest quality customer service to both property owners and tenants using innovative technology and well trained, caring staff.

Vision Statement

To redefine the way in which management is delivered to its customers, becoming the recognized leader in the property management industry.

Brand Essence

When our customers experience our product or service, it brings forth an emotion of absolute trust that we have their best interests at heart

Brand Personality

We are a company that is passionate about our customers, our company and our vision to be leaders in the field of property management. We are visionaries that aren't afraid to use cutting edge technologies to improve our products and service.

Position or Value Proposition

To whom are we speaking?
- real estate investors, including first timers that are giving us their first starter home. They are fairly naive, as they are not "big time" investors, and because they are giving us their first home (in contract to an investor buying a rental property, often sight unseen) they are more emotionally tied to their property and will require a company that inspires trust and confidence.

What is our brand promise?
- we will do our best to serve our clients, both owners and tenants, to give them prompt communication, clear, concise answers to their questions, and look after their property quickly and competently.

Why is our product different than the competition and why should our customers care?
- the current model used by most management companies employs individual portfolio managers that do things a little differently each instance, and differently than their fellow staff members. Our management product is superior because we use a combination of technology and strict procedures to ensure each client's experience is consistent, each and every time.

Industry/Entity Type

Business

Requirements
Must have
• We would like an option to be in black and white, to be able to be printed from Microsoft Word. As well, we do not want anything in a footer or any other kind of letterhead that bleeds below a header. The main use of this letterhead will be from our property management software, to be used in our form letters and other templates (sent to tenants and clients)
Should not have
• Footer or other elements where the text body would be, it will be used in a form letter

```html
<!DOCTYPE html>
<html lang="en">
<head>
<meta charset="utf-8">
<title>Stonebrook Property Management — Letterhead</title>
<link rel="stylesheet" href="https://fonts.googleapis.com/css2?family=Roboto+Condensed:wght@700&display=swap">
<style>
  :root {
    --brand-blue: #1f8fd2;
    --brand-dark: #3b3e42;
    --paper: #ffffff;
    --award-red: #8e1b1f;
  }
  * { margin: 0; padding: 0; box-sizing: border-box; }
  html, body {
    width: 1121px;
    height: 1200px;
    overflow: hidden;
    background: var(--paper);
  }
  .letterhead {
    position: relative;
    width: 1121px;
    height: 1200px;
    background: var(--paper);
    font-family: "Roboto Condensed", "Arial Narrow", sans-serif;
    font-weight: 700;
  }
  .brand {
    position: absolute;
    left: 84px;
    top: 92px;
    display: flex;
    align-items: center;
    gap: 16px;
    color: var(--brand-blue);
  }
  .brand-square {
    width: 56px;
    height: 56px;
    background: var(--brand-dark);
  }
  .brand-name {
    display: flex;
    flex-direction: column;
    line-height: 1;
  }
  .brand-name-main {
    font-size: 44px;
    letter-spacing: 2px;
  }
  .brand-name-sub {
    font-size: 15px;
    letter-spacing: 4.2px;
    margin-top: 4px;
  }
  .contact {
    position: absolute;
    right: 40px;
    top: 68px;
    list-style: none;
    text-align: right;
    color: var(--brand-blue);
  }
  .contact-item {
    display: flex;
    justify-content: flex-end;
    align-items: center;
    gap: 8px;
    height: 19px;
    font-size: 13px;
    white-space: nowrap;
  }
  .contact-item.large { font-size: 17px; height: 21px; }
  .contact-icon {
    width: 15px;
    height: 15px;
    flex: none;
  }
  .header-rule {
    position: absolute;
    left: 0;
    right: 0;
    top: 188px;
    height: 4px;
    background: var(--brand-blue);
  }
  .award-badge {
    position: absolute;
    left: 564px;
    top: 167px;
    width: 46px;
    height: 46px;
    border-radius: 50%;
    background: var(--award-red);
  }
</style>
</head>
<body>
<main class="letterhead">
  <header>
    <div class="brand">
      <div class="brand-square"></div>
      <div class="brand-name">
        <span class="brand-name-main">STONEBROOK</span>
        <span class="brand-name-sub">PROPERTY MANAGEMENT</span>
      </div>
    </div>

    <ul class="contact">
      <li class="contact-item large">204-738-2915
        <svg class="contact-icon" viewBox="0 0 16 16"><circle cx="8" cy="8" r="7" fill="none" stroke="var(--brand-dark)" stroke-width="1.4"/><rect x="5.5" y="3.8" width="5" height="8.4" rx="1" fill="none" stroke="var(--brand-dark)" stroke-width="1.2"/></svg>
      </li>
      <li class="contact-item large">1-888-276-9413
        <svg class="contact-icon" viewBox="0 0 16 16"><circle cx="8" cy="8" r="7.5" fill="var(--brand-dark)"/><rect x="4" y="6.5" width="8" height="4" fill="#fff"/><rect x="5.5" y="4" width="5" height="2" fill="#fff"/></svg>
      </li>
      <li class="contact-item">www.stonebrookpropertymanagement.example
        <svg class="contact-icon" viewBox="0 0 16 16"><circle cx="8" cy="8" r="7.5" fill="var(--brand-dark)"/><circle cx="8" cy="8" r="4" fill="none" stroke="#fff" stroke-width="1.2"/><line x1="4" y1="8" x2="12" y2="8" stroke="#fff" stroke-width="1"/></svg>
      </li>
      <li class="contact-item">C-214 Marlowe Ave, Winnipeg, MB R2K 3P7
        <svg class="contact-icon" viewBox="0 0 16 16"><circle cx="8" cy="8" r="7" fill="none" stroke="var(--brand-dark)" stroke-width="1.4"/><path d="M8 12.5 L5.4 7.8 A3 3 0 1 1 10.6 7.8 Z" fill="none" stroke="var(--brand-dark)" stroke-width="1.2"/></svg>
      </li>
      <li class="contact-item">customerservice@stonebrookpropertymanagement.example
        <svg class="contact-icon" viewBox="0 0 16 16"><circle cx="8" cy="8" r="7.5" fill="var(--brand-dark)"/><rect x="4" y="5.3" width="8" height="5.4" fill="#fff"/><path d="M4 5.3 L8 8.5 L12 5.3" fill="none" stroke="var(--brand-dark)" stroke-width="0.9"/></svg>
      </li>
    </ul>

    <div class="header-rule"></div>

    <div class="award-badge" role="img" aria-label="Resident's Pick Medal award badge"></div>
  </header>
</main>
</body>
</html>
```